LABEL DESIGNS FOR SKINCARE LINE

Hello we are needing 12 label various label designs but would like to see you design ONE. We will pick winner from this and send the rest.
LABEL SIZE -2x7
JAR SIZE IS - 8oz
LOGOS FILES BELOW
https://files.pavorna-share.net/drive/folders/7xk3q-wumTrazPLoqVnnRTZBKHAE2DpLW
INFORMATION FOR LABEL
Calm Dune Hush Whipped Body Sugar Scrub 8oz
Ideal for all Skin Types
Ingredients:
Pure Cane Sugar, Extra Virgin Coconut Oil, Mango Butter, Kukum Butter, Emulsifying Wax, Jojoba Seed Oil, Sweet Almond Oil, Strawberry Essential Oil, and Pomegranate Essential Oil.
Directions to use Body Sugar Scrub:
Apply to wet skin gently in a circular motion on desired body area, hands, feet, legs, arms, etc. Once you have a good scrub, rinse, pat dry, and enjoy soft, hydrated skin. Best to use in the shower. Use between 2-3 times a week if needed.
*Cautions:
(1) Allergy: Approach this product with extreme caution, if you have allergies
(2) Avoid direct contact with eyes
Storage/Shelf Life of Product:
For best results, stir/mix scrub with the wooden or plastic spoon before each use. The shelf life of all sugar scrubs is 6-8 weeks. Keep the product in a cool, dry place, away from hot or heated temperatures.
All Natural, Cruelty-Free, Vegan Free
No Mineral Oil
No Petroleum
No Parabens

```html
<!DOCTYPE html>
<html lang="en">
<head>
<meta charset="UTF-8">
<title>Calm Dune Hush – Body Sugar Scrub Label</title>
<link rel="stylesheet" href="https://fonts.googleapis.com/css2?family=Playfair+Display:wght@400;600;700&family=Montserrat:wght@400;500;600&display=swap">
<style>
  :root {
    --canvas: #ffffff;
    --label-bg: #ffffff;
    --label-edge: #2a2a2a;
    --brand-orange: #e5521a;
    --ink: #151515;
    --ink-soft: #3a3a3a;
    --rose: #e3a3bb;
    --pattern-light: #fbe3ea;
    --pattern-mid: #f3b3c4;
  }
  * { margin: 0; padding: 0; box-sizing: border-box; }
  html, body {
    width: 1200px;
    height: 1200px;
    overflow: hidden;
    background: var(--canvas);
  }
  .canvas {
    position: relative;
    width: 1200px;
    height: 1200px;
  }
  .label {
    position: absolute;
    left: 153px;
    top: 472px;
    width: 894px;
    height: 256px;
    background: var(--label-bg);
    border: 1px solid var(--label-edge);
  }
  .pattern {
    position: absolute;
    top: 0;
    bottom: 0;
    background: linear-gradient(160deg, var(--pattern-light) 0%, var(--pattern-mid) 55%, var(--pattern-light) 100%);
  }
  .pattern--left { left: 233px; width: 127px; }
  .pattern--right { left: 532px; width: 117px; }

  .info-panel {
    position: absolute;
    top: 0;
    height: 100%;
    padding: 16px 16px;
    display: flex;
    flex-direction: column;
    justify-content: center;
    gap: 7px;
    font-family: "Montserrat", sans-serif;
    font-size: 7.4px;
    line-height: 1.35;
    color: var(--ink-soft);
  }
  .info-panel--left { left: 0; width: 233px; }
  .info-panel--right { left: 649px; width: 243px; }
  .info-block__title {
    font-weight: 600;
    font-size: 8px;
    color: var(--ink);
    text-transform: uppercase;
    letter-spacing: 0.6px;
    margin-bottom: 2px;
  }
  .info-block__list { list-style: none; }
  .claims {
    font-weight: 500;
    color: var(--ink);
  }
  .claims span { white-space: nowrap; }

  .front-panel {
    position: absolute;
    left: 360px;
    top: 0;
    width: 172px;
    height: 100%;
    text-align: center;
  }
  .brand-name {
    position: absolute;
    top: 15px;
    left: 0;
    right: 0;
    font-family: "Playfair Display", serif;
    font-weight: 700;
    font-size: 14px;
    color: var(--brand-orange);
    white-space: nowrap;
  }
  .product-name {
    position: absolute;
    top: 76px;
    left: 0;
    right: 0;
    font-family: "Playfair Display", serif;
    line-height: 0.95;
  }
  .product-name__lead {
    display: block;
    font-weight: 600;
    font-size: 27px;
    color: var(--ink);
    letter-spacing: -0.5px;
  }
  .product-name__accent {
    display: block;
    font-weight: 400;
    font-size: 42px;
    color: var(--rose);
    letter-spacing: -1px;
  }
  .product-type {
    position: absolute;
    top: 159px;
    left: 0;
    right: 0;
    font-family: "Montserrat", sans-serif;
    font-size: 12px;
    color: var(--ink);
  }
  .net-weight {
    position: absolute;
    top: 232px;
    left: 0;
    right: 0;
    font-family: "Montserrat", sans-serif;
    font-size: 13px;
    color: var(--ink);
  }
</style>
</head>
<body>
  <main class="canvas">
    <section class="label">
      <div class="info-panel info-panel--left">
        <div class="info-block">
          <h2 class="info-block__title">Ingredients</h2>
          <p>Pure Cane Sugar, Extra Virgin Coconut Oil, Mango Butter, Kukum Butter, Emulsifying Wax, Jojoba Seed Oil, Sweet Almond Oil, Strawberry Essential Oil, and Pomegranate Essential Oil.</p>
        </div>
        <div class="info-block">
          <h2 class="info-block__title">Directions</h2>
          <p>Apply to wet skin gently in a circular motion on desired body area, hands, feet, legs, arms, etc. Once you have a good scrub, rinse, pat dry, and enjoy soft, hydrated skin. Best to use in the shower. Use between 2-3 times a week if needed.</p>
        </div>
        <p class="claims">Ideal for all Skin Types</p>
      </div>

      <div class="pattern pattern--left" role="img" aria-label="Repeating pattern of pink strawberries with green leaves"></div>
      <div class="front-panel">
        <p class="brand-name">Tessa Lune &amp; Co</p>
        <h1 class="product-name">
          <span class="product-name__lead">Calm Dune</span>
          <span class="product-name__accent">Hush</span>
        </h1>
        <p class="product-type">Body Sugar Scrub</p>
        <p class="net-weight">8oz</p>
      </div>
      <div class="pattern pattern--right" role="img" aria-label="Repeating pattern of pink strawberries with green leaves"></div>

      <div class="info-panel info-panel--right">
        <div class="info-block">
          <h2 class="info-block__title">*Cautions</h2>
          <ol class="info-block__list">
            <li>(1) Allergy: Approach this product with extreme caution, if you have allergies</li>
            <li>(2) Avoid direct contact with eyes</li>
          </ol>
        </div>
        <div class="info-block">
          <h2 class="info-block__title">Storage / Shelf Life</h2>
          <p>For best results, stir/mix scrub with the wooden or plastic spoon before each use. The shelf life of all sugar scrubs is 6-8 weeks. Keep the product in a cool, dry place, away from hot or heated temperatures.</p>
        </div>
        <p class="claims">
          <span>All Natural</span> · <span>Cruelty-Free</span> · <span>Vegan Free</span><br>
          <span>No Mineral Oil</span> · <span>No Petroleum</span> · <span>No Parabens</span>
        </p>
      </div>
    </section>
  </main>
</body>
</html>
```